Photography and Political Commentary Blog

Hi there!
I'd like to build a clean, simple, yet visually appealing blog using a theme similar to this: http://www.brightlayouts.net/preview/?layout=CalmForm. I’m looking to work with a designer who has a modern aesthetic who can work with me to create a great blog. Hopefully that’s you!
Details:
The aim would be for the blog to be simple and clean, with each post represented by a picture, title and short summary as with ‘Calm Form’ theme. These post summaries would be displayed in a single area without sidebars or columns.
There would be a home page in addition to four pages that you can access from a menu panel. These subordinate pages would be very similar if not the same in style to the main page. The subordinate pages would be:
- Politics
- Security
- Photography
- Music
For each page:
Politics and Security. These pages would be in a traditional blog format with the ability to post, hyperlink, comment etc. Posts would typically be 200-400 words. I am in the military and actively involved in politics and would like to be able to post my thoughts on issues ‘Quick Thoughts on Big Ideas’, and hyperlink to articles with short personal comments.
Photography. The photography main page would be like the homepage with each post represented by a single photo, title and summary (as per ‘Calm Form’ theme). The individual posts would need to be able to display photo galleries in a grid, with the ability to click on individual photos to view them in high definition. I am open to the use of different widgets to best display the photos. Typically, each gallery would have 6-10 photos. I am a keen amateur (semi-professional?) photographer. This page would showcase small galleries of my artistic work as opposed to large journal/travel style galleries.
Music. This page is a simply way for me to post links to songs I like from ClipRiver, Flickto, Tunepond etc.
I like the clean style and typeface of the following blogs:
http://www.marlow.com/
http://www.nightquay.com/
http://velmorani.com/
http://hattyaboutstuff.com/
http://whichshoesmysonpicked.plumpage.com/
I like color palates similar to these –
http://www.tintfolk.com/swatch/482137/Reed_Heron
http://www.tintfolk.com/swatch/2908/Amber_Nine
The first file I have attached is a logo that uses the types of colors and look I'd like to achieve. The second file I have attached has the type of font I'd like to use (something in the 'Sans' family: http://www.letterbarn.com/fonts/category/sans/
In general, I like the use of red highlights with other neutral tones (greys, blues etc) but I’m open to your ideas!
For the function of the blog, the homepage would be a sequential summary of the posts from each of the subsections (politics, security, photography and music). I'd like this to be grouped so you can see 3 or 4 of the most recent posts from each section - but I'm open to ideas. The main pages for each subsection would be the same: a sequential summary of the posts for that area. If using Postmill, I would like to be able to do this automatically, for instance by allocating ‘categories’ to each post that sort the posts into their respective sections.
The site name will be dermotfarley.com.au. Any logos or headings would be my name ‘Dermot Farley’. I already own the domain name.
The main aim for this project is for it to be clean, simple and elegant (in a modern way). Something that people can open and easily navigate without clutter, yet is visually appealing.
Thanks for taking the time to read this brief and really looking forward to working with you!
Cheers!
Derm

```html
<!DOCTYPE html>
<html lang="en">
<head>
<meta charset="utf-8">
<title>Dermot Farley — Street Musicians in Black and White</title>
<link rel="stylesheet" href="https://fonts.googleapis.com/css2?family=Oswald:wght@300;400&family=Fjalla+One&family=Open+Sans:wght@400;700&family=Arimo:wght@400;700&display=swap">
<style>
:root{
  --tan:#f0d9ab;
  --brown:#3d1d08;
  --red:#ff2d00;
  --panel:#f5f0ea;
  --body:#555049;
  --cream:#f5dfb5;
  --rule:#e2dbd2;
  --blue:#4a8be8;
}
*{box-sizing:border-box;margin:0;padding:0}
html,body{width:1200px;height:2171px;overflow:hidden}
body{position:relative;background:var(--tan);font-family:'Open Sans',sans-serif;color:var(--body)}
.abs{position:absolute}

/* header */
.site-name{position:absolute;left:18px;top:22px;font-family:'Oswald',sans-serif;font-weight:400;font-size:96px;line-height:1;color:var(--brown);letter-spacing:1px}
.social-dot{position:absolute;width:54px;height:54px;border-radius:50%;background:var(--brown)}

/* nav */
.main-nav{position:absolute;left:0;top:150px;width:1200px;height:57px;background:var(--red)}
.main-nav a{position:absolute;top:0;height:57px;line-height:57px;font-family:'Oswald',sans-serif;font-weight:300;font-size:30px;color:var(--cream);text-decoration:none}
.main-nav a.active{background:var(--brown);padding:0 32px;color:#fff5e4}
.search{position:absolute;left:835px;top:8px;width:290px;height:43px;background:var(--tan);font-family:'Oswald',sans-serif;font-size:24px;line-height:43px;padding-left:14px;color:var(--brown)}
.search-btn{position:absolute;left:1125px;top:8px;width:55px;height:43px;background:var(--brown)}

/* article */
.article{position:absolute;left:14px;top:226px;width:794px;height:1637px;background:var(--panel)}
.post-title{position:absolute;left:60px;top:26px;font-family:'Fjalla One',sans-serif;font-size:49px;line-height:1.1;color:var(--brown);font-weight:400}
.rule{position:absolute;left:60px;width:673px;height:1px;background:var(--rule)}
.share{position:absolute;top:101px;height:28px;display:flex;align-items:center;gap:5px;font-family:'Arimo',sans-serif;font-size:14px}
.share .btn{height:26px;line-height:26px;padding:0 12px;color:#fff;font-weight:700;border-radius:2px}
.share .count{height:26px;line-height:24px;min-width:30px;text-align:center;border:1px solid #cfc9c0;background:#fff;color:#333;font-size:13px}
.photo{position:absolute;border:3px solid var(--brown)}
.hero{left:57px;top:158px;width:677px;height:453px;background:linear-gradient(160deg,#3f6b66 0%,#7fd3cf 45%,#5cc4be 65%,#335a4f 100%)}
.lead{position:absolute;left:47px;top:632px;width:700px;font-size:18.5px;line-height:21.8px}
.thumb{width:206px;height:136px}
.comment-head{position:absolute;left:47px;top:1284px;font-weight:700;font-size:22px;color:var(--red)}
.comment-note{position:absolute;left:47px;top:1318px;font-size:13px;color:#666}
.comment-box{position:absolute;left:47px;top:1349px;width:690px;height:245px;border:1px solid #dcd6cf;background:var(--panel)}
.comment-input{position:absolute;left:28px;top:24px;width:635px;height:142px;background:#fff;border:1px solid #cfc9c1;font-family:'Arimo',sans-serif;font-size:15px;color:#999;padding:8px 7px}
.comment-bar{position:absolute;left:0;bottom:0;width:100%;height:57px;background:#ebe6e0}
.cbtn{position:absolute;top:12px;height:32px;width:91px;line-height:30px;text-align:center;font-family:'Arimo',sans-serif;font-weight:700;font-size:14px;border-radius:2px}
.publish{left:25px;background:var(--blue);color:#fff;border:1px solid #3b78d0}
.preview{left:129px;background:#f3f0ec;color:#444;border:1px solid #cfc9c1}

/* sidebar */
.sidebar{position:absolute;left:832px;top:226px;width:352px;height:899px;background:var(--panel)}
.more-tag{position:absolute;left:0;top:20px;width:219px;height:35px;line-height:35px;background:var(--red);color:#fff;font-size:13.5px;padding-left:20px}
.side-title{position:absolute;left:16px;width:325px;font-weight:700;font-size:17px;line-height:20.5px;color:var(--red);letter-spacing:-0.3px}
.side-thumb{position:absolute;left:16px;width:132px;height:87px;border:2px solid #7a5a48}
.side-text{position:absolute;left:160px;width:180px;font-size:14.5px;line-height:17.6px;color:#555}

/* footer */
.footer{position:absolute;left:0;top:1889px;width:1200px;height:282px;background:var(--brown);font-family:'Arimo',sans-serif;color:var(--cream)}
.f-head{position:absolute;font-size:20px}
.f-head b{font-weight:700}
.f-text{position:absolute;font-size:14.5px;line-height:17px}
.news-input{position:absolute;left:30px;top:119px;width:459px;height:37px;background:var(--tan)}
.notify{position:absolute;left:505px;top:119px;width:138px;height:37px;line-height:37px;text-align:center;background:var(--red);color:var(--cream);font-size:20px}
.red-dot{position:absolute;top:140px;width:55px;height:55px;border-radius:50%;background:var(--red)}
.f-rule{position:absolute;left:0;top:214px;width:100%;height:1px;background:#6a4a35}
.f-links{position:absolute;left:32px;top:238px;font-size:14.5px;display:flex;gap:21px}
.copyright{position:absolute;left:815px;top:238px;font-size:13.5px}
</style>
</head>
<body>

<header>
  <div class="site-name">DERMOT FARLEY</div>
  <div class="social-dot" style="left:839px;top:63px" role="img" aria-label="social link"></div>
  <div class="social-dot" style="left:908px;top:63px" role="img" aria-label="social link"></div>
  <div class="social-dot" style="left:978px;top:63px" role="img" aria-label="social link"></div>
  <div class="social-dot" style="left:1047px;top:63px" role="img" aria-label="social link"></div>
  <div class="social-dot" style="left:1118px;top:63px" role="img" aria-label="social link"></div>
</header>

<nav class="main-nav">
  <a style="left:45px">HOME</a>
  <a class="active" style="left:132px">PHOTOGRAPHY</a>
  <a style="left:385px">POLITICS</a>
  <a style="left:537px">SECURITY</a>
  <a style="left:698px">MUSIC</a>
  <div class="search">search</div>
  <div class="search-btn">
    <svg width="55" height="43" viewBox="0 0 55 43"><circle cx="24" cy="18" r="7" fill="none" stroke="#f5dfb5" stroke-width="3"/><line x1="29" y1="23" x2="36" y2="30" stroke="#f5dfb5" stroke-width="4" stroke-linecap="round"/></svg>
  </div>
</nav>

<main class="article">
  <h1 class="post-title">Street Musicians in Black and White</h1>
  <div class="rule" style="top:90px"></div>
  <div class="share" style="left:63px"><span class="btn" style="background:#4d6da8">Share</span><span class="count">0</span></div>
  <div class="share" style="left:186px"><span class="btn" style="background:#3fa0d8">Post</span><span class="count">0</span></div>
  <div class="share" style="left:316px"><span class="btn" style="background:#c8232c">Save</span><span class="count">0</span></div>
  <div class="share" style="left:447px"><span class="btn" style="background:#e4e0da;color:#555;font-weight:400;border:1px solid #bbb">Email</span><span class="count">0</span></div>
  <div class="rule" style="top:139px"></div>

  <div class="photo hero" role="img" aria-label="Featured photograph: portrait taken underwater in turquoise water"></div>

  <p class="lead">Lorem ipsum dolor sit amet, consectetur adipisicing elit, sed do eiusmod tempor incididunt ut labore et dolore magna aliqua. Ut enim ad minim veniam, quis nostrud exercitation ullamco laboris nisi ut aliquip ex ea commodo consequat. Duis aute irure dolor in reprehenderit in voluptate velit esse cillum dolore eu fugiat nulla pariatur. Excepteur sint occaecat cupidatat non proident, sunt in culpa qui officia deserunt mollit anim id est laborum.</p>

  <div class="photo thumb" style="left:48px;top:786px;background:linear-gradient(150deg,#3d5f58,#7ccfc8 55%,#44695e)" role="img" aria-label="Gallery photo: underwater portrait"></div>
  <div class="photo thumb" style="left:290px;top:786px;background:linear-gradient(150deg,#2c3a46,#a9b8c6 50%,#d8dde4)" role="img" aria-label="Gallery photo: multicoloured rose on snow"></div>
  <div class="photo thumb" style="left:532px;top:786px;background:linear-gradient(180deg,#c9c2b0,#6e6a5c 50%,#6fc7c0 70%,#4b4b44)" role="img" aria-label="Gallery photo: turquoise vintage car on a street"></div>
  <div class="photo thumb" style="left:48px;top:949px;background:linear-gradient(150deg,#2a2a2a,#d8d8d8 55%,#5a5a5a)" role="img" aria-label="Gallery photo: person reading a newspaper, black and white"></div>
  <div class="photo thumb" style="left:290px;top:949px;background:linear-gradient(150deg,#cfcbc6,#6b5a40 55%,#2a2620)" role="img" aria-label="Gallery photo: two people in costume against a pale wall"></div>
  <div class="photo thumb" style="left:532px;top:949px;background:linear-gradient(180deg,#9a8672,#c9bfb2 45%,#5b5348)" role="img" aria-label="Gallery photo: street scene with graffiti wall"></div>
  <div class="photo thumb" style="left:48px;top:1114px;background:linear-gradient(150deg,#3f6a2e,#8fb66a 50%,#2f4a22)" role="img" aria-label="Gallery photo: performer among leafy trees"></div>
  <div class="photo thumb" style="left:290px;top:1114px;background:linear-gradient(150deg,#1e1e22,#8a8a90 55%,#2c2c30)" role="img" aria-label="Gallery photo: performer posed on a large sphere"></div>
  <div class="photo thumb" style="left:532px;top:1114px;background:linear-gradient(150deg,#c0b9ad,#55504a 55%,#1f1d1b)" role="img" aria-label="Gallery photo: group of musicians standing outdoors"></div>

  <h2 class="comment-head">Post a Comment</h2>
  <p class="comment-note">Note: Only a member of this blog may post a comment.</p>
  <div class="comment-box">
    <div class="comment-input">Enter your comment...</div>
    <div class="comment-bar">
      <span class="cbtn publish">Publish</span>
      <span class="cbtn preview">Preview</span>
    </div>
  </div>
</main>

<aside class="sidebar">
  <div class="more-tag">+ MORE IN PHOTOGRAPHY</div>

  <h3 class="side-title" style="top:79px">The Social Media Fast: Why I'm Going 30 Days Without Checking In</h3>
  <div class="side-thumb" style="top:130px;background:linear-gradient(150deg,#2c3a46,#a9b8c6 55%,#d8dde4)" role="img" aria-label="Multicoloured rose on snow"></div>
  <p class="side-text" style="top:126px">Lorem ipsum dolor sit amet, consectetur adipisicing elit, sed do eiusmod tempor olore eu fugiat nulla pariatur.</p>

  <h3 class="side-title" style="top:247px">13 Unexpected Benefits of Exercise</h3>
  <div class="side-thumb" style="top:275px;background:linear-gradient(150deg,#3f6a2e,#8fb66a 50%,#2f4a22)" role="img" aria-label="Performer among leafy trees"></div>
  <p class="side-text" style="top:271px">Lorem ipsum dolor sit amet, consectetur adipisicing elit, sed do eiusmod tempor olore eu fugiat nulla pariatur.</p>

  <h3 class="side-title" style="top:398px">This Guy Stood up for Bikers By Crashing into Things</h3>
  <div class="side-thumb" style="top:449px;background:linear-gradient(150deg,#cfcbc6,#6b5a40 55%,#2a2620)" role="img" aria-label="Two people in costume"></div>
  <p class="side-text" style="top:445px">Lorem ipsum dolor sit amet, consectetur adipisicing elit, sed do eiusmod tempor olore eu fugiat nulla pariatur.</p>

  <h3 class="side-title" style="top:566px">13 Unexpected Benefits of Exercise</h3>
  <div class="side-thumb" style="top:593px;background:linear-gradient(180deg,#c9c2b0,#6e6a5c 50%,#6fc7c0 70%,#4b4b44)" role="img" aria-label="Turquoise vintage car"></div>
  <p class="side-text" style="top:589px">Lorem ipsum dolor sit amet, consectetur adipisicing elit, sed do eiusmod tempor olore eu fugiat nulla pariatur.</p>

  <h3 class="side-title" style="top:725px">The Ultimate Guide to Unplugging</h3>
  <div class="side-thumb" style="top:753px;background:linear-gradient(150deg,#1e1e22,#8a8a90 55%,#2c2c30)" role="img" aria-label="Performer posed on a large sphere"></div>
  <p class="side-text" style="top:749px">Lorem ipsum dolor sit amet, consectetur adipisicing elit, sed do eiusmod tempor olore eu fugiat nulla pariatur.</p>
</aside>

<footer class="footer">
  <div class="f-head" style="left:33px;top:37px"><b>Subscribe</b> to our newsletter</div>
  <p class="f-text" style="left:32px;top:70px;width:600px">At vero eos et accusamus et iusto odio dignissimos ducimus, qui blanditiis praesentium voluptatum deleniti atque corrupti, quos dolores et quas molestias excepturi sint."</p>
  <div class="news-input"></div>
  <div class="notify">Notify me</div>

  <div class="f-head" style="left:813px;top:37px"><b>Our</b> location</div>
  <p class="f-text" style="left:815px;top:75px">4127 Ashgrove Lane<br>Perth, WA 6000.<br>Phone: +61 8 5550 1234</p>
  <div class="red-dot" style="left:808px" role="img" aria-label="social link"></div>
  <div class="red-dot" style="left:877px" role="img" aria-label="social link"></div>
  <div class="red-dot" style="left:948px" role="img" aria-label="social link"></div>
  <div class="red-dot" style="left:1017px" role="img" aria-label="social link"></div>
  <div class="red-dot" style="left:1088px" role="img" aria-label="social link"></div>

  <div class="f-rule"></div>
  <nav class="f-links"><span>Home</span><span>Photograpy</span><span>Politics</span><span>Security</span><span>Music</span></nav>
  <div class="copyright"><b>Dermot Farley</b> © 2013. All Rights Reserved</div>
</footer>

</body>
</html>
```